Kestrel Ridge Trophies & Awards Unique Business Card Design

Recently selected a new logo design and waiting to recieve print files. I've attached image for your review. We are a trophies and awards company that provides engraving on trophies, plaques, name plates, name tags, desk sets, medals, acrylics, and signage.

We are located in Monroe, Louisiana and provide this service with computerized & laser engraving equipment.

Target Market(s)

Corporate, Sport, Church, and Special Events

Industry/Entity Type

Business

Contact Information for Business Card

I'd like to see the following list on the card: Trophies, Plaques, Name Plates, Name Tags, Desk Sets, Medals, Certificates... this is accomplished with Computerized & Laser Engraving

Colors
0555a3
ec1f27
ffffff

Requirements
Must have
• I like either single or double sided. If a design can be created with a frosted card stock I'd consider single. Must be Red, White, and Blue. Dalton Wrenfield - Owner, 418 W 9th Ave, Monroe, La 71201 office 318-555-0186 fax 318-555-0142 email: kestrel@kestrelridgetrophiesawards.example, and website: www.kestrelridgetrophiesawards.example

```html
<!DOCTYPE html>
<html lang="en">
<head>
<meta charset="utf-8">
<title>Kestrel Ridge Trophies &amp; Awards – Business Card</title>
<link rel="stylesheet" href="https://fonts.googleapis.com/css2?family=Montserrat:wght@500&family=Open+Sans:wght@400;700&display=swap">
<style>
  :root {
    --bg: #2f2b28;
    --card-black: #141414;
    --card-black-light: #262626;
    --brand-blue: #0555a3;
    --band-blue: #1f63c9;
    --band-blue-light: #3b82e6;
    --brand-red: #ec1f27;
    --white: #ffffff;
    --text-grey: #a9a9a9;
    --logo-blue: #2f74d8;
  }
  html, body {
    margin: 0;
    width: 1200px;
    height: 844px;
    overflow: hidden;
    background: var(--bg);
  }
  .canvas {
    position: relative;
    width: 1200px;
    height: 844px;
  }
  .card {
    position: absolute;
    top: 279px;
    width: 500px;
    height: 286px;
    background: linear-gradient(135deg, var(--card-black) 0%, var(--card-black-light) 55%, var(--card-black) 100%);
    overflow: hidden;
    box-shadow: 0 10px 30px rgba(0,0,0,0.45);
  }
  .card--back { left: 60px; }
  .card--front { left: 640px; }

  /* Back: contact side */
  .band {
    position: absolute;
    left: 0;
    width: 100%;
    height: 12px;
    background: linear-gradient(90deg, var(--band-blue), var(--band-blue-light));
  }
  .band--top { top: 0; }
  .band--bottom { bottom: 0; }
  .rule-red {
    position: absolute;
    left: 0;
    width: 100%;
    height: 4px;
    background: var(--brand-red);
  }
  .rule-red--top { top: 16px; }
  .rule-red--bottom { bottom: 16px; }

  .identity {
    position: absolute;
    top: 62px;
    left: 0;
    width: 100%;
    text-align: center;
  }
  .identity__name {
    display: inline-block;
    font-family: 'Montserrat', sans-serif;
    font-weight: 500;
    font-size: 17px;
    letter-spacing: 0.5px;
    color: var(--white);
    padding: 0 4px 3px;
    border-bottom: 2px solid var(--brand-blue);
  }
  .identity__title {
    margin-top: 4px;
    font-family: 'Open Sans', sans-serif;
    font-size: 13px;
    color: var(--text-grey);
  }
  .contacts {
    position: absolute;
    top: 136px;
    left: 0;
    width: 100%;
    margin: 0;
    padding: 0;
    list-style: none;
    text-align: center;
    font-family: 'Open Sans', sans-serif;
    font-size: 13px;
    line-height: 18px;
    color: var(--text-grey);
    white-space: nowrap;
  }
  .contacts__address { margin-top: 10px; }

  /* Front: brand side */
  .brand {
    position: absolute;
    top: 50%;
    left: 50%;
    transform: translate(-50%, -50%);
    text-align: center;
    white-space: nowrap;
  }
  .brand__rule {
    height: 2px;
    background: var(--logo-blue);
  }
  .brand__line {
    display: flex;
    align-items: center;
    justify-content: center;
    gap: 8px;
    padding: 8px 6px;
    font-family: 'Open Sans', sans-serif;
    font-weight: 700;
    font-size: 24px;
    color: var(--logo-blue);
  }
  .brand__dot {
    width: 12px;
    height: 12px;
    border-radius: 50%;
    background: var(--brand-red);
  }
  .tab {
    position: absolute;
    width: 30px;
    height: 46px;
    background: linear-gradient(180deg, var(--band-blue-light), var(--band-blue));
  }
  .tab--left {
    left: 0;
    top: 180px;
    border-right: 4px solid var(--brand-red);
  }
  .tab--right {
    right: 0;
    top: 40px;
    border-left: 4px solid var(--brand-red);
  }
</style>
</head>
<body>
<main class="canvas">
  <section class="card card--back" aria-label="Business card, contact side">
    <div class="band band--top"></div>
    <div class="rule-red rule-red--top"></div>

    <div class="identity">
      <div class="identity__name">DALTON WRENFIELD</div>
      <div class="identity__title">Owner</div>
    </div>

    <ul class="contacts">
      <li>318-555-0186</li>
      <li>318-555-0142</li>
      <li>kestrel@kestrelridgetrophiesawards.example</li>
      <li>www.kestrelridgetrophiesawards.example</li>
      <li class="contacts__address">418 W 9th Ave | Monroe, LA | 71201</li>
    </ul>

    <div class="rule-red rule-red--bottom"></div>
    <div class="band band--bottom"></div>
  </section>

  <section class="card card--front" aria-label="Business card, brand side">
    <div class="tab tab--right"></div>
    <div class="brand">
      <div class="brand__rule"></div>
      <div class="brand__line">
        <span class="brand__dot"></span>
        <span class="brand__name">Kestrel Ridge Trophies &amp; Awards</span>
      </div>
      <div class="brand__rule"></div>
    </div>
    <div class="tab tab--left"></div>
  </section>
</main>
</body>
</html>
```